Meadowlark Recovery Brochure

We need a brochure template we can change photo's and words at a later date. WE offer rehabilitation to injured horses and ponies.
Either use our Meadowlark Grounds or Meadowlark Recovery logo but not both. A strong preference for the horse being led to feature first.

Target Market(s)

Horse Owners

Font styles to use
Serif

Colors
f78f20

Requirements
Must have
• Ability to write the text and interchange photos within the layout at a later date.
Nice to have
• Our colours are orange and black

```html
<!DOCTYPE html>
<html lang="en">
<head>
<meta charset="utf-8">
<title>Meadowlark Recovery – Tri-fold Brochure</title>
<link rel="stylesheet" href="https://fonts.googleapis.com/css2?family=Cinzel:wght@400;700&family=Cormorant+Garamond:wght@500;600&family=Great+Vibes&family=Open+Sans:wght@600&family=Oswald:wght@600&display=swap">
<style>
  :root {
    --brand-orange: #e2533a;
    --paper: #ffffff;
    --page-bg: #eeeeee;
    --ink-light: #ffffff;
    --strip-grey: #e9e6e3;
    --title-font: "Cinzel", serif;
    --body-font: "Cormorant Garamond", serif;
    --script-font: "Great Vibes", cursive;
    --list-font: "Open Sans", sans-serif;
    --label-font: "Oswald", sans-serif;
  }
  * { box-sizing: border-box; margin: 0; padding: 0; }
  html, body { width: 904px; height: 1200px; overflow: hidden; }
  body { background: var(--page-bg); position: relative; }

  .spread {
    position: absolute; left: 38px; width: 828px; height: 555px;
    background: var(--paper); overflow: hidden;
    box-shadow: 0 6px 18px rgba(0,0,0,.18);
  }
  .spread--outside { top: 30px; }
  .spread--inside { top: 615px; }

  .panel { position: absolute; top: 0; width: 276px; height: 555px; overflow: hidden; }
  .panel--1 { left: 0; }
  .panel--2 { left: 276px; }
  .panel--3 { left: 552px; }

  .block { position: absolute; left: 0; width: 100%; }
  .block--orange { background: var(--brand-orange); color: var(--ink-light); }
  .photo { position: absolute; }

  .section-title {
    font-family: var(--title-font); font-weight: 700; font-size: 13px;
    letter-spacing: .5px; text-align: center; color: var(--ink-light);
  }
  .section-title::after {
    content: ""; display: block; width: 90px; height: 1px;
    background: rgba(255,255,255,.8); margin: 4px auto 0;
  }
  .body-copy {
    font-family: var(--body-font); font-weight: 500; font-size: 13.5px;
    line-height: 1.25; text-align: center; color: var(--ink-light);
  }

  /* Outside: cover tagline */
  .tagline { text-align: center; padding-top: 16px; }
  .tagline__small { font-family: var(--title-font); font-size: 13px; letter-spacing: 6px; line-height: 16px; }
  .tagline__small--minor { font-size: 11px; letter-spacing: 4px; line-height: 14px; }
  .tagline__script { font-family: var(--script-font); font-size: 54px; line-height: 48px; margin-top: 2px; }
  .tagline__bold { font-family: var(--title-font); font-weight: 700; font-size: 20px; letter-spacing: 1px; line-height: 24px; }
  .tagline__bold--minor { font-size: 16px; line-height: 20px; }
  .tagline__rule { width: 150px; height: 1px; background: rgba(255,255,255,.8); margin: 5px auto; }

  /* Contact */
  .contact { text-align: center; }
  .contact__icon { display: block; margin: 0 auto 6px; }
  .contact__phone { font-family: var(--title-font); font-weight: 700; font-size: 19px; margin-bottom: 14px; }
  .contact__line { font-family: var(--body-font); font-weight: 600; font-size: 15px; line-height: 1.2; margin-bottom: 14px; }

  /* Brand */
  .brand {
    display: flex; align-items: center; justify-content: center; gap: 10px; height: 100%;
  }
  .brand__name {
    font-family: var(--title-font); font-weight: 400; font-size: 22px;
    line-height: 1.05; color: var(--brand-orange); text-align: right;
  }
  .brand__mark { width: 44px; height: 44px; background: var(--brand-orange); }

  .back-tagline { text-align: center; padding-top: 22px; }
  .back-tagline__small { font-family: var(--title-font); font-size: 11px; letter-spacing: 4px; }
  .back-tagline__big { font-family: var(--title-font); font-weight: 700; font-size: 36px; line-height: 1; margin: 4px 0; }
  .back-tagline__mid { font-family: var(--title-font); font-weight: 700; font-size: 16px; }

  /* Inside */
  .gallery-strip {
    position: absolute; left: 0; top: 240px; width: 40px; height: 315px;
    background: var(--strip-grey); display: flex; align-items: center; justify-content: center;
  }
  .gallery-strip__label {
    font-family: var(--label-font); font-weight: 600; font-size: 19px; color: var(--brand-orange);
    letter-spacing: .5px; transform: rotate(-90deg); white-space: nowrap;
  }
  .services-title {
    font-family: var(--title-font); font-weight: 700; font-size: 20px; line-height: 1.05;
    padding: 26px 22px 0;
  }
  .services-title::after {
    content: ""; display: block; width: 150px; height: 1px; background: rgba(255,255,255,.8); margin-top: 6px;
  }
  .services-list { list-style: none; padding: 18px 22px 0; }
  .services-list li {
    font-family: var(--list-font); font-weight: 600; font-size: 16px; line-height: 1.15;
    display: flex; gap: 10px; margin-bottom: 8px;
  }
  .services-list svg { flex: none; margin-top: 3px; }
</style>
</head>
<body>

<!-- Outside spread -->
<section class="spread spread--outside">
  <div class="panel panel--1">
    <div class="photo" style="left:0;top:0;width:276px;height:390px;background:linear-gradient(160deg,#9a7f66 0%,#4a4a46 45%,#2c2a28 100%);" role="img" aria-label="Photo: caregiver treating a wound on a horse's leg"></div>
    <div class="block block--orange" style="top:390px;height:165px;">
      <div class="tagline">
        <div class="tagline__small">REMARKABLE</div>
        <div class="tagline__script">Care</div>
        <div class="tagline__bold">AND TREATMENT</div>
        <div class="tagline__rule"></div>
        <div class="tagline__small tagline__small--minor">FOR REMARKABLE</div>
        <div class="tagline__bold tagline__bold--minor">HORSES</div>
      </div>
    </div>
  </div>

  <div class="panel panel--2">
    <div class="block block--orange" style="top:0;height:475px;padding:28px 24px 0;">
      <h2 class="section-title">OUR MISSION</h2>
      <p class="body-copy" style="margin-top:12px;">Lorem ipsum dolor Lorem ipsum dolor sit amet, consectetuer adipiscing elit, sed diam nonummy nibh euismod tincidunt ut laoreet consectetuer adipiscing elit, sed diam nonummy nibh euismod tincidunt ut laoreet</p>
      <h2 class="section-title" style="margin-top:26px;">CONTACT US</h2>
      <div class="contact" style="margin-top:14px;">
        <svg class="contact__icon" width="26" height="26" viewBox="0 0 26 26" fill="none" stroke="#fff" stroke-width="1.3"><circle cx="13" cy="13" r="12"/><path d="M9.5 7.5l2 2.5-1.3 1.5c.8 1.8 2 3 3.8 3.8l1.5-1.3 2.5 2-1 1.8c-4.3-.5-8-4.2-8.5-8.5z"/></svg>
        <div class="contact__phone">303-555-0148</div>
        <svg class="contact__icon" width="26" height="26" viewBox="0 0 26 26" fill="none" stroke="#fff" stroke-width="1.3"><circle cx="13" cy="13" r="12"/><path d="M13 19.5s-4.5-4.5-4.5-8a4.5 4.5 0 0 1 9 0c0 3.5-4.5 8-4.5 8z"/><circle cx="13" cy="11.5" r="1.5"/></svg>
        <div class="contact__line">1180 Larkspur Lane<br>Larkfield, CO 80999</div>
        <svg class="contact__icon" width="26" height="26" viewBox="0 0 26 26" fill="none" stroke="#fff" stroke-width="1.3"><circle cx="13" cy="13" r="12"/><rect x="7.5" y="9" width="11" height="8"/><path d="M7.5 9l5.5 4.5L18.5 9"/></svg>
        <div class="contact__line">info@meadowlark<br>recovery.com</div>
      </div>
    </div>
    <div class="photo" style="left:0;top:475px;width:276px;height:80px;background:linear-gradient(180deg,#6f7a4e 0%,#8a7a62 100%);" role="img" aria-label="Photo: shaded dirt path through the grounds"></div>
  </div>

  <div class="panel panel--3">
    <div class="block" style="top:0;height:150px;">
      <div class="brand">
        <div class="brand__name">MEADOWLARK<br>RECOVERY</div>
        <div class="brand__mark"></div>
      </div>
    </div>
    <div class="photo" style="left:0;top:150px;width:276px;height:250px;background:linear-gradient(150deg,#6b6a48 0%,#8d6a45 40%,#3e4a3a 100%);" role="img" aria-label="Photo: handler leading a chestnut horse along a tree-lined lane"></div>
    <div class="block block--orange" style="top:400px;height:155px;">
      <div class="back-tagline">
        <div class="back-tagline__small">WE HELP IN GIVING</div>
        <div class="back-tagline__big">LIFE BACK</div>
        <div class="back-tagline__small" style="font-size:10px;">TO YOUR</div>
        <div class="back-tagline__mid">HORSES AND PONIES.</div>
      </div>
    </div>
  </div>
</section>

<!-- Inside spread -->
<section class="spread spread--inside">
  <div class="panel panel--1">
    <div class="block block--orange" style="top:0;height:300px;padding:30px 26px 0;">
      <h2 class="section-title">ABOUT US</h2>
      <p class="body-copy" style="margin-top:14px;">Lorem ipsum dolor Lorem ipsum dolor sit amet, consectetuer adipiscing elit, sed diam nonummy nibh euismod tincidunt ut laoreet consectetuer adipiscing elit, sed diam nonummy nibh euismod tincidunt ut laoreet</p>
      <p class="body-copy" style="margin-top:12px;">sed diam nonummy nibh euismod tincidunt ut laoreet consectetuer adipiscing elit, sed diam nonummy nibh euismod tincidunt ut laoreet</p>
    </div>
    <div class="photo" style="left:0;top:300px;width:138px;height:125px;background:linear-gradient(160deg,#7a4a32 0%,#5a2a22 100%);" role="img" aria-label="Photo: horse leg wound before treatment"></div>
    <div class="photo" style="left:138px;top:300px;width:138px;height:125px;background:linear-gradient(160deg,#a0603c 0%,#7a4a30 100%);" role="img" aria-label="Photo: same leg healed after treatment"></div>
    <div class="photo" style="left:0;top:425px;width:276px;height:130px;background:linear-gradient(180deg,#4f7e8a 0%,#9a6a48 50%,#5e8f96 100%);" role="img" aria-label="Photo: horse swimming in the rehabilitation pool"></div>
  </div>

  <div class="panel panel--2">
    <div class="photo" style="left:0;top:0;width:276px;height:240px;background:linear-gradient(160deg,#8c8a7e 0%,#7a4e30 45%,#6e7a4a 100%);" role="img" aria-label="Photo: mare grazing beside her foal"></div>
    <div class="gallery-strip"><span class="gallery-strip__label">REHABILITATION GALLARY</span></div>
    <div class="photo" style="left:40px;top:240px;width:236px;height:160px;background:linear-gradient(160deg,#c9c4bc 0%,#3a3430 55%,#6a5442 100%);" role="img" aria-label="Photo: horse exercising on an underwater treadmill"></div>
    <div class="photo" style="left:40px;top:400px;width:236px;height:155px;background:linear-gradient(160deg,#b8b3ac 0%,#5a4a3e 50%,#3a2e28 100%);" role="img" aria-label="Photo: therapist giving a horse chiropractic treatment"></div>
  </div>

  <div class="panel panel--3">
    <div class="photo" style="left:0;top:0;width:276px;height:200px;background:linear-gradient(160deg,#8f8c80 0%,#6e7a4a 100%);" role="img" aria-label="Photo: paddock and arena fencing"></div>
    <div class="block block--orange" style="top:200px;height:355px;">
      <h2 class="services-title">REHABILITATION<br>SERVICES</h2>
      <ul class="services-list">
        <li><svg width="12" height="12" viewBox="0 0 12 12"><path d="M2 1l8 5-8 5z" fill="#fff"/></svg>Aqua Treadmill</li>
        <li><svg width="12" height="12" viewBox="0 0 12 12"><path d="M2 1l8 5-8 5z" fill="#fff"/></svg>Free Swimming Pool</li>
        <li><svg width="12" height="12" viewBox="0 0 12 12"><path d="M2 1l8 5-8 5z" fill="#fff"/></svg>Cold Salt Chambers</li>
        <li><svg width="12" height="12" viewBox="0 0 12 12"><path d="M2 1l8 5-8 5z" fill="#fff"/></svg>Vibration Plate/solarium</li>
        <li><svg width="12" height="12" viewBox="0 0 12 12"><path d="M2 1l8 5-8 5z" fill="#fff"/></svg>Cold Laser Therapy</li>
        <li><svg width="12" height="12" viewBox="0 0 12 12"><path d="M2 1l8 5-8 5z" fill="#fff"/></svg>Equine Ultrasound</li>
        <li><svg width="12" height="12" viewBox="0 0 12 12"><path d="M2 1l8 5-8 5z" fill="#fff"/></svg>Breathing Therapy</li>
        <li><svg width="12" height="12" viewBox="0 0 12 12"><path d="M2 1l8 5-8 5z" fill="#fff"/></svg>Equine Chiropractic<br>&amp; Massage</li>
      </ul>
    </div>
  </div>
</section>

</body>
</html>
```